Business Card Design

I would like a new business card design for an accounting firm that specializes in resolving clients tax problems. I want the card to give the impression that we are not your typical stodgy accounting firm, but at the same time we will get the job done.
Industry/Entity Type
Business
Contact Information for Business Card
Marcus T Kelbeck
Certified Public Accountant
27-08 63rd Avenue
Brinmore, NY 10492
Tel: (718) 555-0143
Fax: (888) 555-0176
e-mail: mtkledger@quillpost.net
website: harborstonefiscalaidgroup.com

```html
<!DOCTYPE html>
<html lang="en">
<head>
<meta charset="utf-8">
<title>Marcus T Kelbeck — Business Card</title>
<link rel="stylesheet" href="https://fonts.googleapis.com/css2?family=Cinzel:wght@400;500&family=Crimson+Pro:wght@400&display=swap">
<style>
  :root {
    --page-bg: #5a5a5a;
    --card-white: #ffffff;
    --card-black: #050505;
    --ink-dark: #1a1a1a;
    --ink-grey: #4a4a4a;
    --ink-light: #f4f4f4;
    --rule-light: #9a9a9a;
    --skyline-tone: #d9d9d9;
  }
  * { box-sizing: border-box; margin: 0; padding: 0; }
  html, body {
    width: 1105px; height: 1200px; overflow: hidden;
    background: var(--page-bg);
  }
  .canvas { position: relative; width: 1105px; height: 1200px; }

  .card {
    position: absolute; left: 196px; width: 720px; height: 411px; overflow: hidden;
  }
  .card--front { top: 146px; background: var(--card-white); }
  .card--back { top: 602px; background: var(--card-black); }

  .skyline-main {
    position: absolute; left: 186px; top: 58px; width: 342px; height: 79px;
    background: linear-gradient(to bottom, #ffffff 0%, var(--skyline-tone) 100%);
  }
  .skyline-small {
    position: absolute; left: 585px; top: 222px; width: 135px; height: 38px;
    background: linear-gradient(to bottom, #ffffff 0%, var(--skyline-tone) 100%);
  }
  .divider-line {
    position: absolute; left: 0; right: 0; top: 260px; height: 2px; background: var(--ink-dark);
  }

  .holder-name {
    position: absolute; left: 0; right: 0; top: 149px; text-align: center;
    font-family: "Cinzel", serif; font-weight: 500; font-size: 31px; line-height: 40px;
    text-transform: uppercase; letter-spacing: 0.5px; color: var(--ink-dark);
  }
  .holder-title {
    position: absolute; left: 0; right: 0; top: 190px; text-align: center;
    font-family: "Cinzel", serif; font-weight: 400; font-size: 20px; line-height: 24px;
    letter-spacing: 1px; color: var(--ink-grey);
  }

  .contact-band {
    position: absolute; left: 0; right: 0; top: 264px; bottom: 0;
    background: var(--card-black); color: var(--ink-light);
    font-family: "Crimson Pro", serif; font-size: 21px; line-height: 27px; text-align: center;
  }
  .contact-address { position: absolute; left: 0; right: 0; top: 28px; }
  .contact-lines {
    position: absolute; left: 0; right: 0; top: 64px;
    display: flex; justify-content: center; align-items: center; gap: 12px;
  }
  .contact-item { display: inline-flex; align-items: center; gap: 7px; }
  .contact-item svg { width: 15px; height: 15px; fill: var(--ink-light); }
  .contact-web { position: absolute; left: 0; right: 0; top: 99px; }

  .association-name {
    position: absolute; left: 0; right: 0; top: 196px; text-align: center;
    font-family: "Crimson Pro", serif; font-weight: 400; font-size: 30px; line-height: 36px;
    color: var(--ink-light);
  }
  .association-tagline {
    position: absolute; left: 129px; width: 462px; top: 240px;
    display: flex; align-items: center; gap: 10px;
    font-family: "Crimson Pro", serif; font-size: 8px; letter-spacing: 1.5px;
    text-transform: uppercase; color: var(--ink-light); white-space: nowrap;
  }
  .association-tagline::before,
  .association-tagline::after {
    content: ""; flex: 1; height: 1px; background: var(--rule-light);
  }
</style>
</head>
<body>
<main class="canvas">
  <section class="card card--front">
    <div class="skyline-main" role="img" aria-label="Line drawing of a city skyline with the Statue of Liberty"></div>
    <h1 class="holder-name">Marcus T Kelbeck</h1>
    <p class="holder-title">Certified Public Accountant</p>
    <div class="skyline-small" role="img" aria-label="Small line drawing of a city skyline"></div>
    <div class="divider-line"></div>
    <div class="contact-band">
      <p class="contact-address">27-08 63rd Avenue, Brinmore, NY 10492</p>
      <p class="contact-lines">
        <span class="contact-item">
          <svg viewBox="0 0 16 16" aria-hidden="true"><path d="M3.6 1.2l2.3 2.6-1.3 1.9c.9 2 2.6 3.7 4.6 4.6l1.9-1.3 2.6 2.3-1.4 2.3C7.2 15 1 8.8 1.3 2.6z"/></svg>
          (718) 555-0143
        </span>
        <span class="contact-item">
          <svg viewBox="0 0 16 16" aria-hidden="true"><path d="M4 1h7l1 1v3H4z M1 6h14v6h-3v3H4v-3H1z M5 10v4h6v-4z"/></svg>
          (888) 555-0176
        </span>
        <span class="contact-item">
          <svg viewBox="0 0 16 16" aria-hidden="true"><path d="M1 3h14v1.2L8 9 1 4.2z M1 5.6l7 4.8 7-4.8V13H1z"/></svg>
          mtkledger@quillpost.net
        </span>
      </p>
      <p class="contact-web">www.harborstonefiscalaidgroup.com</p>
    </div>
  </section>

  <section class="card card--back">
    <p class="association-name">Coastal Alliance of Tax Resolvers</p>
    <p class="association-tagline">A Non-Profit Professional Association</p>
  </section>
</main>
</body>
</html>
```